Business card design for a dynamic IT consulting company

We need a business card design for a young firm, specialized in the Telecommunications/Consulting industry. The name of the company is Brask and Partners Business Consulting Ltd. (Short name: Brask and Partnes)
Brask = solve read reverse, so we aim to be uncomplicated and solution-oriented. The small pipe in our logo is also related to the word solve. So we need a new business card design, which is simple, eye catching and something non traditional (I would probably prefer a square shaped design rather than a rectangle, but open for suggestions). Attached our logo.

Target Market(s)

Usually our customers are Tier1 Telecoms providers (Q-Linkra, Parnexo, etc) and their executives.

Industry/Entity Type

Business

Contact Information for Business Card

Name: Gergely Halmindo
Email: g.halmindo@braskpartnera.hu
Web: www.braskpartnera.hu
Mobile: +36 30 555 0192
Title: Managing Director

Optional:
Company name: Brask and Partners Ltd.
Address: 1047 Budapest, Ravaszi str. 17/B, Hungary

Font styles to use
Other font styles liked:
• helveticaneue_medium, Prime Regular are used now.

Colors

Designer to choose colors to be used in the design.

Requirements
Must have
• I would like to have a 2 sided design.
Nice to have
• I thought if we make the logo a bit bigger (without the company name), that could go to the back with the company name below. I though, if the pipe in the logo is somehow touchable on the business card, would be nice and unique.

```html
<!DOCTYPE html>
<html lang="en">
<head>
<meta charset="utf-8">
<title>Brask and Partners – Business Card</title>
<link href="https://fonts.googleapis.com/css2?family=Roboto:wght@400;500&display=swap" rel="stylesheet">
<style>
  :root {
    --bg: #8c8c8c;
    --card-white: #f7f7f7;
    --card-dark: #202020;
    --strip-dark: #262626;
    --blue: #1a8fd0;
    --magenta: #c0259a;
    --grey-bar: #5a5a5a;
    --text-dark: #444444;
    --rule: #9a9a9a;
    --emboss: #4a4a4a;
    --white: #ffffff;
  }
  * { margin: 0; padding: 0; box-sizing: border-box; }
  html, body {
    width: 1200px; height: 1134px; overflow: hidden;
    background: var(--bg);
    font-family: "Roboto", Arial, sans-serif;
  }
  .card {
    position: absolute; left: 261px;
    width: 675px; height: 381px;
    border-radius: 18px; overflow: hidden;
  }
  .card-front { top: 161px; background: var(--card-white); }
  .card-back { top: 589px; background: var(--card-dark); }

  .brand-strip {
    position: absolute; left: 0; top: 0;
    width: 119px; height: 100%;
    background: var(--strip-dark);
  }
  .brand-strip .wordmark {
    position: absolute; left: 60px; top: 150px;
    transform: translate(-50%, -50%) rotate(-90deg);
    white-space: nowrap;
    font-size: 27px; font-weight: 400; color: var(--white);
  }
  .brand-strip .mark-square {
    position: absolute; left: 44px; top: 306px;
    width: 32px; height: 32px; background: var(--white);
  }
  .accent-bars { position: absolute; left: 122px; top: 0; width: 7px; height: 100%; }
  .accent-bars span { position: absolute; left: 0; width: 100%; }
  .bar-blue { top: 0; height: 123px; background: var(--blue); }
  .bar-magenta { top: 123px; height: 129px; background: var(--magenta); }
  .bar-grey { top: 252px; height: 129px; background: var(--grey-bar); }

  .person { position: absolute; left: 164px; top: 56px; }
  .person-name { font-size: 28px; font-weight: 500; line-height: 1.2; }
  .first-name { color: var(--blue); }
  .last-name { color: var(--magenta); font-weight: 400; }
  .person-title { font-size: 18px; color: var(--text-dark); }

  .company { position: absolute; left: 164px; top: 200px; width: 329px; }
  .company-name { font-size: 16px; color: var(--blue); line-height: 22px; }
  .company-address { font-size: 15.5px; color: var(--text-dark); line-height: 22px; }
  .company-rule { margin-top: 9px; height: 2px; background: var(--rule); }

  .contacts { position: absolute; left: 164px; top: 268px; list-style: none; }
  .contacts li {
    display: flex; align-items: center; height: 25.5px;
    font-size: 15.5px; color: var(--text-dark);
  }
  .contacts .icon {
    width: 20px; height: 20px; border-radius: 3px; margin-right: 9px;
    display: flex; align-items: center; justify-content: center;
  }
  .icon-phone { background: var(--blue); }
  .icon-mail { background: var(--magenta); }
  .icon-web { background: var(--grey-bar); }

  .back-mark {
    position: absolute; left: 50%; top: 130px;
    width: 40px; height: 40px; margin-left: -20px;
    background: var(--emboss);
  }
  .back-wordmark {
    position: absolute; left: 0; top: 222px; width: 100%;
    text-align: center; font-size: 40px; font-weight: 400;
    color: var(--emboss);
  }
</style>
</head>
<body>
  <section class="card card-front">
    <div class="brand-strip">
      <div class="wordmark">Brask &amp; Partners</div>
      <div class="mark-square"></div>
    </div>
    <div class="accent-bars">
      <span class="bar-blue"></span><span class="bar-magenta"></span><span class="bar-grey"></span>
    </div>

    <div class="person">
      <div class="person-name"><span class="first-name">Gergely</span> <span class="last-name">Halmindo</span></div>
      <div class="person-title">Managing Director</div>
    </div>

    <div class="company">
      <div class="company-name">Brask and Partners Ltd</div>
      <div class="company-address">1047 Budapest, Ravaszi str. 17/B, Hungary</div>
      <div class="company-rule"></div>
    </div>

    <ul class="contacts">
      <li><span class="icon icon-phone">
        <svg width="12" height="12" viewBox="0 0 24 24"><path fill="#fff" d="M6.6 10.8a15.1 15.1 0 0 0 6.6 6.6l2.2-2.2c.3-.3.7-.4 1-.2 1.1.4 2.3.6 3.6.6.6 0 1 .4 1 1V20c0 .6-.4 1-1 1A17 17 0 0 1 3 4c0-.6.4-1 1-1h3.5c.6 0 1 .4 1 1 0 1.3.2 2.5.6 3.6.1.3 0 .7-.2 1z"/></svg>
      </span>801.555.0147</li>
      <li><span class="icon icon-mail">
        <svg width="12" height="10" viewBox="0 0 24 18"><rect x="1" y="1" width="22" height="16" fill="none" stroke="#fff" stroke-width="2"/><path d="M1 1l11 9 11-9" fill="none" stroke="#fff" stroke-width="2"/></svg>
      </span>g.halmindo@braskpartnera.hu</li>
      <li><span class="icon icon-web">
        <svg width="12" height="12" viewBox="0 0 24 24"><circle cx="12" cy="12" r="10" fill="none" stroke="#fff" stroke-width="2"/><path d="M2 12h20M12 2c3 3 3 17 0 20M12 2c-3 3-3 17 0 20" fill="none" stroke="#fff" stroke-width="2"/></svg>
      </span>www.braskpartnera.hu</li>
    </ul>
  </section>

  <section class="card card-back">
    <div class="back-mark"></div>
    <div class="back-wordmark">Brask &amp; Partners</div>
  </section>
</body>
</html>
```